Traffic product supplier - Temporary Raised Pavement Markers

We need a flyer design that will grab the customer's eye to the product (TRPMs) and entice curiosity to the business. Showing 1 product but promoting other products. The following information should be included:
- Logo (attached)
- Sale Product image (Temporary Road Pavement Marker AKA Press and Holds)
- Product wording (attached word document)

Happy for you to add/amend wording for grammatical purpose and other images that show it is a sale flyer.

Background on KLV - We are a thermoplastic manufacturer for road markings and traffic product supplier. KLV specializes in producing high quality hotmelt thermoplastic that meet Australian Standard AS4049.2. We are able to produce other specifications as required by the customer.

Would like the colour scheme to be similar to the logo.

If you need more information let me know.

Target Market(s)

Asphalt industry / road builders

Font styles to use
Serif
Sans Serif

Requirements
Must have
• - Kelvoro Lane Ventures (My company name)
- Contact details:
- 02 8417 2530
- marcus.t@klvsupplyco.com.au
- info@klvsupplyco.com.au
-www.klvmtq.com

- Attached images.
-Title (Temporary Road Pavement Markers)

```html
<!DOCTYPE html>
<html lang="en">
<head>
<meta charset="utf-8">
<title>Kelvoro Lane Ventures – Temporary Road Pavement Markers</title>
<link rel="stylesheet" href="https://fonts.googleapis.com/css2?family=Montserrat:wght@700;800&family=Mulish:wght@400;600&display=swap">
<style>
  :root{
    --brand-blue:#1b5fae;
    --deep-blue:#1450a0;
    --ink:#3a3a3c;
    --text:#444;
    --yellow:#f2c500;
    --marker-yellow:#e0b12c;
    --marker-white:#e3e4e5;
    --paper:#f1f1f0;
    --stage:#e4e4e4;
  }
  *{box-sizing:border-box;margin:0;padding:0}
  html,body{width:1200px;height:857px;overflow:hidden;background:var(--stage)}
  .flyer{position:absolute;left:300px;top:26px;width:600px;height:804px;overflow:hidden;
    background:linear-gradient(180deg,#e9ecef 0%,#dfe3e6 30%,var(--paper) 55%,var(--paper) 100%);
    font-family:"Mulish",Arial,sans-serif;color:var(--text)}
  .brand{position:absolute;left:0;right:0;top:46px;display:flex;justify-content:center;align-items:center;gap:10px}
  .brand-mark{width:22px;height:22px;background:var(--brand-blue)}
  .brand-name{font-family:"Montserrat",Arial,sans-serif;font-weight:800;font-size:48px;color:var(--brand-blue);letter-spacing:2px}
  .headline{position:absolute;left:0;right:0;top:128px;text-align:center;font-family:"Montserrat",Arial,sans-serif;font-weight:800;line-height:35px}
  .headline .line1{display:block;font-size:26px;color:var(--brand-blue)}
  .headline .line2{display:block;font-size:26px;color:var(--ink)}
  .scene{position:absolute;left:0;top:215px;width:600px;height:290px}

  .marker-group{position:absolute}
  .marker{position:absolute;border-radius:3px;box-shadow:0 3px 6px rgba(0,0,0,.18)}
  .marker.yellow{background:linear-gradient(180deg,#e9c43c 0%,var(--marker-yellow) 18%,#d9a928 100%)}
  .marker.red-white{background:linear-gradient(180deg,#e0474f 0%,#e0474f 14%,var(--marker-white) 15%,#dadcdd 100%)}
  .marker.white{background:linear-gradient(180deg,#c9cdd1 0%,#c9cdd1 12%,var(--marker-white) 13%,#d8dadb 100%)}

  .hero-products{left:0;top:0;width:600px;height:480px}
  .hero-products .yellow{left:31px;top:269px;width:199px;height:120px}
  .hero-products .red-white{left:175px;top:289px;width:215px;height:125px}
  .hero-products .white{left:323px;top:324px;width:248px;height:143px}

  .section{position:absolute}
  .section h2{font-family:"Montserrat",Arial,sans-serif;font-weight:800;font-size:16px;color:var(--brand-blue);margin-bottom:5px}
  .section p{font-size:10.5px;line-height:13.2px;text-align:justify}
  .use{left:28px;top:435px;width:255px}
  .product{left:28px;top:559px;width:255px}
  .dims{left:316px;top:486px;width:265px}
  .dims ul{list-style:none}
  .dims li{position:relative;padding-left:16px;font-size:10.3px;font-weight:600;color:#333;line-height:13px;margin-bottom:10px}
  .dims li svg{position:absolute;left:2px;top:2px}
  .footer-bg{position:absolute;left:0;top:0}

  .footer-products{left:0;top:0;width:600px;height:804px}
  .footer-products .white{left:316px;top:620px;width:154px;height:108px}
  .footer-products .yellow{left:356px;top:645px;width:160px;height:112px}
  .footer-products .red-white{left:420px;top:683px;width:154px;height:106px}

  .company{position:absolute;left:28px;top:726px;font-family:"Montserrat",Arial,sans-serif;font-weight:700;font-size:15px;color:var(--yellow)}
  .contacts{position:absolute;left:28px;top:750px;display:grid;grid-template-columns:121px auto;row-gap:2px;font-size:10.5px;color:#fff}
  .contacts span{display:flex;align-items:center;gap:5px;white-space:nowrap}
</style>
</head>
<body>
<main class="flyer">
  <svg class="scene" width="600" height="290" viewBox="0 0 600 290" role="img" aria-label="Photo of a dual carriageway motorway running through autumn fields and trees">
    <defs>
      <linearGradient id="land" x1="0" y1="0" x2="0" y2="1">
        <stop offset="0" stop-color="#9a9a7a"/>
        <stop offset="0.5" stop-color="#8b8a64"/>
        <stop offset="1" stop-color="#6f6f5c"/>
      </linearGradient>
    </defs>
    <rect x="0" y="0" width="600" height="240" fill="url(#land)"/>
    <path d="M0 148 Q300 152 600 226 L600 290 L0 290Z" fill="var(--paper)"/>
    <path d="M0 139 Q300 140 600 196 L600 226 Q300 152 0 148Z" fill="var(--yellow)"/>
  </svg>

  <div class="brand"><span class="brand-mark"></span><span class="brand-name">KLV</span></div>

  <h1 class="headline"><span class="line1">CREATING A SAFE ENVIRONMENT</span><span class="line2">FOR ALL ROAD USERS</span></h1>

  <div class="marker-group hero-products" role="img" aria-label="Three temporary road pavement markers in yellow, white with red strip and all white">
    <span class="marker yellow"></span>
    <span class="marker red-white"></span>
    <span class="marker white"></span>
  </div>

  <section class="section use">
    <h2>USE/GENERAL DESCRIPTION:</h2>
    <p>Temporary road pavement markers, also known as press ‘n’ holds, are a great short-term solution to mark asphalt and pavements before permanent line marking takes place. They provide a way to delineate lanes and edges before the permanent longitudinal line marking process takes place.</p>
  </section>

  <section class="section product">
    <h2>PRODUCT DESCRIPTION:</h2>
    <p>TRPMs or press ‘n’ holds are available in yellow or white and come with a Class 1A reflective strip applied to tough high impact plastic. They are an economical solution for making newly laid roads safer. An easy to remove clear cover protects the reflective film during sealing and is easily ripped off afterwards.</p>
  </section>

  <section class="section dims">
    <h2>DIMENSIONS:</h2>
    <ul>
      <li><svg width="9" height="9" viewBox="0 0 10 10"><circle cx="5" cy="5" r="5" fill="var(--brand-blue)"/><path d="M2.7 5.2 L4.3 6.8 L7.3 3.6" stroke="#fff" stroke-width="1.4" fill="none"/></svg>100 mm long x 50 mm high x 25 mm wide</li>
      <li><svg width="9" height="9" viewBox="0 0 10 10"><circle cx="5" cy="5" r="5" fill="var(--brand-blue)"/><path d="M2.7 5.2 L4.3 6.8 L7.3 3.6" stroke="#fff" stroke-width="1.4" fill="none"/></svg>Double sided Class 1A Reflective</li>
      <li><svg width="9" height="9" viewBox="0 0 10 10"><circle cx="5" cy="5" r="5" fill="var(--brand-blue)"/><path d="M2.7 5.2 L4.3 6.8 L7.3 3.6" stroke="#fff" stroke-width="1.4" fill="none"/></svg>Clear cover for reflective protection</li>
      <li><svg width="9" height="9" viewBox="0 0 10 10"><circle cx="5" cy="5" r="5" fill="var(--brand-blue)"/><path d="M2.7 5.2 L4.3 6.8 L7.3 3.6" stroke="#fff" stroke-width="1.4" fill="none"/></svg>Available in all white, and red (reflective strip) and white, all yellow and all blue</li>
    </ul>
  </section>

  <svg class="footer-bg" width="600" height="804" viewBox="0 0 600 804" aria-hidden="true">
    <path d="M0 694 Q250 690 420 712 Q520 726 600 762 L600 804 L0 804Z" fill="var(--deep-blue)"/>
    <path d="M0 684 Q250 680 420 702 Q520 716 600 751 L600 763 Q520 727 420 713 Q250 691 0 695Z" fill="var(--yellow)"/>
  </svg>

  <div class="marker-group footer-products" role="img" aria-label="Group of three temporary pavement markers: white, yellow and white with red strip">
    <span class="marker white"></span>
    <span class="marker yellow"></span>
    <span class="marker red-white"></span>
  </div>

  <p class="company">KELVORO LANE VENTURES</p>
  <div class="contacts">
    <span><svg width="10" height="10" viewBox="0 0 10 10"><path d="M2 1 L3.8 1 L4.4 3 L3.2 4 Q4.2 6 6 6.8 L7 5.6 L9 6.2 L9 8 Q9 9 8 9 Q1 8.5 1 2 Q1 1 2 1Z" fill="var(--yellow)"/></svg>02 8417 2530</span>
    <span><svg width="10" height="10" viewBox="0 0 10 10"><rect x="0.5" y="2" width="9" height="6" fill="var(--yellow)"/><path d="M0.5 2 L5 5.5 L9.5 2" stroke="var(--deep-blue)" stroke-width="0.9" fill="none"/></svg>marcus.t@klvsupplyco.com.au</span>
    <span><svg width="10" height="10" viewBox="0 0 10 10"><circle cx="5" cy="5" r="4.2" fill="none" stroke="var(--yellow)" stroke-width="1.1"/><path d="M0.8 5 H9.2 M5 0.8 Q2.5 5 5 9.2 M5 0.8 Q7.5 5 5 9.2" stroke="var(--yellow)" stroke-width="0.8" fill="none"/></svg>www.klvmtq.com</span>
    <span><svg width="10" height="10" viewBox="0 0 10 10"><rect x="0.5" y="2" width="9" height="6" fill="var(--yellow)"/><path d="M0.5 2 L5 5.5 L9.5 2" stroke="var(--deep-blue)" stroke-width="0.9" fill="none"/></svg>info@klvsupplyco.com.au</span>
  </div>
</main>
</body>
</html>
```